Kfz-Werkstatt sucht Design
Zielgruppe
Kfz-Werkstatt / Kunden
Aufgabenstellung
Flyer Format: DIN A5 lang
Text:
Wir ziehen um....
Ab 03.07.2017 finden Sie uns in neuen Räumlichkeiten

```html
<!DOCTYPE html>
<html lang="de">
<head>
<meta charset="utf-8">
<title>Wir ziehen um – Bernd Kohlmann Kfz-Technik</title>
<link href="https://fonts.googleapis.com/css2?family=Arimo:wght@400;700&display=swap" rel="stylesheet">
<style>
  :root {
    --paper: #ffffff;
    --brand-blue: #1d55a5;
    --label-grey: #8c8c8c;
    --text-grey: #7f7f7f;
    --line-grey: #8a8a8a;
  }
  * { margin: 0; padding: 0; box-sizing: border-box; }
  html, body { width: 846px; height: 1200px; overflow: hidden; background: var(--paper); }
  .flyer {
    position: relative;
    width: 846px;
    height: 1200px;
    background: var(--paper);
    font-family: "Arimo", Arial, sans-serif;
    color: var(--text-grey);
  }
  .brand {
    position: absolute;
    top: 108px;
    left: 0;
    width: 846px;
    display: flex;
    justify-content: center;
    align-items: center;
    gap: 12px;
  }
  .brand-dot {
    width: 22px;
    height: 22px;
    border-radius: 50%;
    background: var(--brand-blue);
  }
  .brand-name {
    font-weight: 700;
    font-size: 24px;
    letter-spacing: 1px;
    color: var(--brand-blue);
  }
  .headline {
    position: absolute;
    left: 207px;
    top: 225px;
    width: 456px;
    height: 88px;
    background: var(--label-grey);
    border-radius: 12px;
    box-shadow: 4px 6px 10px rgba(0,0,0,0.25);
    color: #fff;
    font-weight: 700;
    font-size: 54px;
    line-height: 88px;
    text-align: center;
  }
  .connector {
    position: absolute;
    left: 0;
    top: 0;
  }
  .tools-visual {
    position: absolute;
    left: 210px;
    top: 355px;
    width: 460px;
    height: 420px;
    background: linear-gradient(180deg, #eaf0f8 0%, #d6e1f1 100%);
    border-radius: 6px;
  }
  .move-note {
    position: absolute;
    left: 207px;
    top: 862px;
    font-size: 25px;
    line-height: 33px;
  }
  .move-note strong { font-weight: 700; }
  .new-address {
    position: absolute;
    left: 207px;
    top: 958px;
    font-style: normal;
    font-weight: 700;
    font-size: 25px;
    line-height: 36px;
  }
</style>
</head>
<body>
  <main class="flyer">
    <header class="brand">
      <span class="brand-dot"></span>
      <span class="brand-name">BERND KOHLMANN</span>
    </header>

    <h1 class="headline">Wir ziehen um</h1>

    <svg class="connector" width="846" height="1200" viewBox="0 0 846 1200" aria-hidden="true">
      <polyline points="663,270 805,270 805,1035 590,1035" fill="none" stroke="var(--line-grey)" stroke-width="3"/>
      <polygon points="572,1035 594,1023 594,1047" fill="var(--line-grey)"/>
    </svg>

    <div class="tools-visual" role="img" aria-label="Blaue Illustration von Werkzeugen: Ringschlüssel, Schraubendreher und Hammer"></div>

    <p class="move-note">Ab <strong>03.07.2017</strong> finden Sie uns in<br>neuen Räumlichkeiten:</p>

    <address class="new-address">
      Bernd Kohlmann<br>
      Kfz-Technik<br>
      Lindenweg 12b<br>
      31234 Musterhausen<br>
      Tel.: 05100 48260
    </address>
  </main>
</body>
</html>
```